Domestic Cleaning services needs a website

We need a descriptive, easy to use and trust inspiring website for domestic cleaning clients. It should be easy to use, with appointment scheduling and SMS notifiers. The brand name "BrightNest by Marisol" should be associated with all offers at the website. blue/green/white colors should be more pronounced.
Website should be Mobile friendly.

Target Market(s)

Domestic Market. Long rental tourists, expats, local housewifes

Logo Text

BRIGHTNEST by MARISOL

Number of Pages Required

2 page

Font styles to use
Sans Serif

```html
<!DOCTYPE html>
<html lang="en">
<head>
<meta charset="utf-8">
<title>BrightNest by Marisol – Domestic Cleaning</title>
<link href="https://fonts.googleapis.com/css2?family=Fira+Sans:wght@400;500;600;700&family=Open+Sans:wght@400;600;700&family=Poppins:wght@400;600&display=swap" rel="stylesheet">
<style>
:root{
  --teal:#0b504d;
  --teal-light:#1a6662;
  --teal-band:#0d4a47;
  --orange:#f26a36;
  --yellow:#f5b51d;
  --ink:#333;
  --muted:#666;
  --gray-bg:#f2f2f2;
  --card:#f0f0f0;
  --white:#fff;
}
*{box-sizing:border-box;margin:0;padding:0}
html,body{width:1200px;height:2995px;overflow:hidden}
body{position:relative;font-family:"Open Sans",sans-serif;color:var(--ink);background:var(--white)}
.abs{position:absolute}

/* header */
.site-header{left:0;top:0;width:1200px;height:150px;background:var(--teal)}
.brand-block{left:0;top:0;width:296px;height:150px;background:var(--teal-light)}
.contact-row{left:316px;top:22px;width:860px;height:48px}
.contact-item{position:absolute;top:0;display:flex;gap:16px;align-items:flex-start;color:var(--white)}
.contact-item svg{width:26px;height:26px;flex:none;margin-top:2px}
.contact-item small{display:block;font-size:12px;line-height:18px}
.contact-item strong{display:block;font-size:12px;line-height:20px;font-weight:700}
.header-rule{left:296px;top:86px;width:904px;height:1px;background:rgba(255,255,255,.18)}
.main-nav{left:326px;top:108px;display:flex;gap:34px;font-family:"Fira Sans",sans-serif;font-weight:600;font-size:15px;color:var(--white)}
.main-nav .active{color:var(--yellow)}

/* hero */
.hero-photo{left:0;top:150px;width:1200px;height:464px;background:linear-gradient(100deg,#c8cfcc 0%,#e4e6e3 40%,#d9d6cf 70%,#efefed 100%)}
.hero-disc{left:92px;top:212px;width:328px;height:328px;border-radius:50%;background:rgba(40,40,40,.82);text-align:center;color:var(--white)}
.hero-kicker{margin-top:106px;font-family:"Poppins",sans-serif;font-size:27px;color:var(--yellow)}
.hero-title{font-family:"Poppins",sans-serif;font-weight:600;font-size:27px;line-height:38px}
.hero-text{margin:10px auto 0;width:224px;font-size:12px;line-height:24px}
.hero-btn{display:inline-block;margin-top:10px;width:152px;height:34px;line-height:34px;background:var(--yellow);font-family:"Fira Sans",sans-serif;font-size:13px;font-weight:600}
.promo-badge{left:54px;top:206px;width:122px;height:122px;border-radius:50%;background:var(--yellow);color:var(--white);text-align:center;transform:rotate(-18deg)}
.promo-badge small{display:block;margin-top:20px;font-size:12px;font-weight:600}
.promo-badge b{display:block;font-family:"Fira Sans",sans-serif;font-size:38px;line-height:38px}
.promo-badge i{display:block;font-style:normal;font-size:8px;line-height:10px;padding:0 24px}

/* info band */
.info-band{left:0;top:614px;width:1200px;height:114px;background:var(--teal-band)}
.info-item{position:absolute;top:32px;display:flex;gap:22px;color:var(--white)}
.info-item svg{width:36px;height:36px;flex:none}
.info-item strong{display:block;font-family:"Fira Sans",sans-serif;font-size:13px;font-weight:600;line-height:22px}
.info-item span{font-size:12px;line-height:22px}
.plus{position:absolute;top:46px;width:22px;height:22px;border-radius:50%;background:var(--yellow);color:var(--white);font-size:18px;line-height:22px;text-align:center;font-weight:700}
.band-divider{position:absolute;top:24px;width:1px;height:68px;background:rgba(255,255,255,.25)}

/* appointment */
.appointment{left:0;top:728px;width:1200px;height:534px;background:var(--gray-bg)}
.section-title{position:absolute;left:0;width:1200px;text-align:center;font-family:"Fira Sans",sans-serif;font-weight:600;font-size:32px}
.section-lead{position:absolute;left:110px;width:980px;text-align:center;font-size:11px;line-height:24px;color:var(--muted)}
.appointment .section-title{top:42px;color:#3a3a3a}
.appointment .section-lead{top:110px}
.steps{position:absolute;left:110px;top:188px;width:980px;display:flex;gap:4px}
.step{flex:1;font-size:12px;color:#555}
.step::after{content:"";display:block;margin-top:6px;height:10px;background:#c9c9c9}
.step.current{color:var(--orange)}
.step.current::after{background:var(--orange)}
.form-note{left:110px;top:246px;font-size:12px}
.field{position:absolute;top:284px;width:236px}
.field label{display:block;font-size:12px;color:var(--orange);margin-bottom:8px}
.select{height:28px;border:1px solid #ccc;background:var(--white);font-size:11px;line-height:26px;padding:0 8px;position:relative}
.select::after{content:"";position:absolute;right:8px;top:11px;border:4px solid transparent;border-top:5px solid #444}
.row-label{position:absolute;font-size:12px}
.date-box{left:110px;top:382px;width:154px;height:28px;border:1px solid #ccc;background:var(--white);font-size:11px;line-height:26px;padding-left:8px}
.day{position:absolute;top:358px;width:30px;text-align:center;font-size:12px}
.day i{display:block;margin:10px auto 0;width:22px;height:22px;border-radius:50%;background:var(--orange);position:relative}
.day i::after{content:"";position:absolute;left:8px;top:4px;width:5px;height:10px;border:solid var(--white);border-width:0 2px 2px 0;transform:rotate(45deg)}
.small-select{position:absolute;top:382px;height:28px}
.next-btn{left:986px;top:464px;width:104px;height:32px;background:var(--orange);color:var(--white);text-align:center;line-height:32px;font-family:"Fira Sans",sans-serif;font-weight:600;font-size:14px}

/* services */
.services{left:0;top:1262px;width:1200px;height:682px;background:var(--white)}
.services .section-title{top:46px;color:#3a3a3a}
.services .section-lead{top:112px}
.services-ring{left:418px;top:232px;width:364px;height:364px;border-radius:50%;border:2px solid #d6e1e0;background:radial-gradient(circle,#6a8a7a 0%,#2f5e52 55%,#a8b8b0 100%)}
.service-thumb{position:absolute;width:112px;height:112px;border-radius:50%;border:6px solid var(--white);box-shadow:0 0 0 1px #ddd}
.service{position:absolute;width:250px}
.service h3{font-family:"Fira Sans",sans-serif;font-weight:600;font-size:15px;color:var(--teal)}
.service p{font-size:11px;line-height:17px;color:var(--muted);margin-top:4px}
.service.left{text-align:right}

/* why choose */
.why{left:0;top:1944px;width:600px;height:612px;background:var(--teal)}
.why-photo{left:600px;top:1944px;width:600px;height:612px;background:linear-gradient(135deg,#5a4a3a 0%,#8a7a60 45%,#2f4f45 75%,#c9b56a 100%)}
.why h2{position:absolute;left:0;top:70px;width:422px;text-align:center;font-family:"Fira Sans",sans-serif;font-weight:600;font-size:30px;color:var(--white)}
.feature{position:absolute;width:220px;color:var(--white)}
.feature .badge{position:absolute;left:-56px;top:0;width:28px;height:28px;border-radius:50%;background:var(--yellow)}
.feature .badge svg{width:28px;height:28px}
.feature h3{font-family:"Fira Sans",sans-serif;font-weight:600;font-size:16px;line-height:22px}
.feature p{font-size:11px;line-height:20px;margin-top:16px}

/* testimonials */
.testimonials-title{left:0;top:2596px;width:1200px;text-align:center;font-family:"Fira Sans",sans-serif;font-weight:600;font-size:30px;color:var(--teal)}
.testimonial{position:absolute;top:2664px;width:474px;height:188px;background:var(--card)}
.avatar{position:absolute;left:18px;top:30px;width:76px;height:76px;border-radius:50%;background:linear-gradient(160deg,#c49a6c,#6b4a30);border:3px solid var(--white)}
.testimonial p{position:absolute;left:136px;top:26px;width:310px;font-size:11px;line-height:22px;color:var(--muted)}
.testimonial strong{position:absolute;left:136px;top:106px;font-size:12px}
.testimonial span{position:absolute;left:136px;top:148px;font-size:11px;color:var(--muted)}

/* footer */
.site-footer{left:0;top:2906px;width:1200px;height:89px;background:var(--teal);color:var(--white);font-size:11px;padding:40px 0 0 116px}
</style>
</head>
<body>

<header class="abs site-header">
  <div class="abs brand-block"></div>
  <div class="abs contact-row">
    <div class="contact-item" style="left:0">
      <svg viewBox="0 0 24 24" fill="none" stroke="#f5b51d" stroke-width="1.8"><path d="M5 3h4l2 5-3 2a12 12 0 0 0 6 6l2-3 5 2v4a2 2 0 0 1-2 2A17 17 0 0 1 3 5a2 2 0 0 1 2-2z"/></svg>
      <div><small>We're On Call 24/7</small><strong>+62-150-480-37</strong></div>
    </div>
    <div class="contact-item" style="left:250px">
      <svg viewBox="0 0 24 24" fill="none" stroke="#f5b51d" stroke-width="1.8"><rect x="2" y="6" width="20" height="13"/><path d="M2 6l10 8 10-8"/></svg>
      <div><small>Need Customer Support?</small><strong>hello@brightnest.example</strong></div>
    </div>
    <div class="contact-item" style="left:560px">
      <svg viewBox="0 0 24 24" fill="none" stroke="#f5b51d" stroke-width="1.8"><path d="M7 10v11H3V10zM7 10l4-8a3 3 0 0 1 3 3v4h6a2 2 0 0 1 2 2l-2 8a2 2 0 0 1-2 2H7"/></svg>
      <div><small>Guarantee For Services</small><strong>6 Months Guarantee</strong></div>
    </div>
  </div>
  <div class="abs header-rule"></div>
  <nav class="abs main-nav">
    <span class="active">HOME</span><span>ABOUT US</span><span>OUR SERVICES</span><span>OUR CONTACT</span><span>LOGIN</span>
  </nav>
</header>

<section>
  <div class="abs hero-photo" role="img" aria-label="Photo of a smiling cleaner in a green apron with colleagues cleaning windows behind her"></div>
  <div class="abs hero-disc">
    <div class="hero-kicker">Clean Home</div>
    <div class="hero-title">BrightNest by Marisol</div>
    <p class="hero-text">Hi omnes lingua, institutis, legibus inter se differunt. Quo usque tandem abutere</p>
    <span class="hero-btn">READ MORE</span>
  </div>
  <div class="abs promo-badge"><small>Discount</small><b>20%</b><i>Off For Home Cleaning Service Only</i></div>
</section>

<section class="abs info-band">
  <div class="info-item" style="left:116px">
    <svg viewBox="0 0 36 36" fill="none" stroke="#f5b51d" stroke-width="2"><circle cx="18" cy="18" r="15"/><path d="M18 9v9l6 4"/></svg>
    <div><strong>Operating Hours</strong><span>Monday - Friday 08:00 - 20:00</span></div>
  </div>
  <div class="plus" style="left:398px">+</div>
  <div class="band-divider" style="left:436px"></div>
  <div class="info-item" style="left:456px">
    <svg viewBox="0 0 36 36" fill="none" stroke="#f5b51d" stroke-width="2"><path d="M4 18L18 5l14 13M8 15v16h8v-9h4v9h8V15"/></svg>
    <div><strong>Our Office Location</strong><span>48 Harbor Lane, Westvale, XYZ</span></div>
  </div>
  <div class="plus" style="left:732px">+</div>
  <div class="band-divider" style="left:770px"></div>
  <div class="info-item" style="left:790px">
    <svg viewBox="0 0 36 36" fill="none" stroke="#f5b51d" stroke-width="2"><path d="M4 18L18 4h13v13L17 31z"/><circle cx="25" cy="11" r="2"/></svg>
    <div><strong>Promotion Offers</strong><span>Summer Madness and Superfast</span></div>
  </div>
  <div class="plus" style="left:1066px">+</div>
</section>

<section class="abs appointment">
  <h2 class="section-title">Make an Appointment</h2>
  <p class="section-lead">Nihil hic munitissimus habendi senatus locus, nihil horum? Quisque ut dolor gravida, placerat libero vel, euismod. Quo usque tandem abutere, Catilina, patientia nostra? Quis aute iure reprehenderit in voluptate velit esse. Petierunt uti sibi concilium totius Galliae in diem certam indicere.</p>
  <div class="steps">
    <div class="step current">1. Service</div><div class="step">2. Time</div><div class="step">3. Details</div><div class="step">4. Payment</div><div class="step">5. Done</div>
  </div>
  <p class="abs form-note">Please select service:</p>
  <div class="field" style="left:110px"><label>Category</label><div class="select">Select category</div></div>
  <div class="field" style="left:358px"><label>Service</label><div class="select">Select service</div></div>
  <div class="field" style="left:606px"><label>Employee</label><div class="select">Any</div></div>
  <div class="field" style="left:854px"><label>Number of persons</label><div class="select">1</div></div>
  <span class="row-label" style="left:110px;top:358px">I'm available on or after</span>
  <div class="abs date-box">January 6, 2017</div>
  <div class="day" style="left:278px">Mon<i></i></div>
  <div class="day" style="left:309px">Tue<i></i></div>
  <div class="day" style="left:340px">Wed<i></i></div>
  <div class="day" style="left:371px">Thu<i></i></div>
  <div class="day" style="left:402px">Fri<i></i></div>
  <div class="day" style="left:433px">Sat<i></i></div>
  <div class="day" style="left:464px">Sun<i></i></div>
  <span class="row-label" style="left:508px;top:358px">Start from</span>
  <div class="select small-select" style="left:508px;width:84px">8:00 am</div>
  <span class="row-label" style="left:604px;top:358px">Finish by</span>
  <div class="select small-select" style="left:604px;width:84px">6:00 pm</div>
  <div class="abs next-btn">NEXT</div>
</section>

<section class="abs services">
  <h2 class="section-title">Our Professional Services</h2>
  <p class="section-lead">Nihil hic munitissimus habendi senatus locus, nihil horum? Quisque ut dolor gravida, placerat libero vel, euismod. Quo usque tandem abutere, Catilina, patientia nostra? Quis aute iure reprehenderit in voluptate velit esse. Petierunt uti sibi concilium totius Galliae in diem certam indicere.</p>
  <div class="abs services-ring" role="img" aria-label="Photo of a cleaner in a green apron mopping"></div>
  <div class="service-thumb" style="left:444px;top:208px;background:#b9a8c8" role="img" aria-label="Photo of a gloved hand wiping a surface"></div>
  <div class="service-thumb" style="left:638px;top:208px;background:#6f7478" role="img" aria-label="Photo of a car wheel being washed"></div>
  <div class="service-thumb" style="left:410px;top:366px;background:#3b6fc4" role="img" aria-label="Photo of a worker cleaning a building facade"></div>
  <div class="service-thumb" style="left:720px;top:366px;background:#7a8fa8" role="img" aria-label="Photo of a maintenance technician at work"></div>
  <div class="service-thumb" style="left:454px;top:512px;background:#c8c0b0" role="img" aria-label="Photo of a cleaner in an office"></div>
  <div class="service-thumb" style="left:652px;top:508px;background:#a9b7a4" role="img" aria-label="Photo of a pest control worker spraying"></div>
  <div class="service left" style="left:182px;top:214px"><h3>Home Cleaning</h3><p>Curabitur blandit tempus porttitor praesent commodo cursus magna vel</p></div>
  <div class="service" style="left:768px;top:218px"><h3>Vehicle Cleaning</h3><p>Cras justo odio, dapibus ac facilisis in, egestas eget quam maecenas sagittis tru</p></div>
  <div class="service left" style="left:148px;top:376px"><h3>Building Cleaning</h3><p>Etiam porta sem males uada magna mollis euismod donec ullamcorper</p></div>
  <div class="service" style="left:842px;top:388px"><h3>Maintenance Service</h3><p>Aenean lacinia bibendum nulla sed consectetur hum sociis natoque</p></div>
  <div class="service left" style="left:186px;top:550px"><h3>Commercial Cleaning</h3><p>Nulla vitae elit libero, a pharetra augue maecenas faucibus mollis interdum</p></div>
  <div class="service" style="left:762px;top:554px"><h3>Pest Control</h3><p>Cum sociis natoque penatibus et magnis dis parturient montes nascetur</p></div>
</section>

<section class="abs why">
  <h2>Why Choose Us?</h2>
  <div class="feature" style="left:106px;top:148px"><span class="badge"><svg viewBox="0 0 28 28" fill="none" stroke="#fff" stroke-width="1.6"><rect x="9" y="9" width="10" height="10" rx="1"/><path d="M9 13h10"/></svg></span><h3>Online Appointment</h3><p>Lorem ipsum dolor sit amet, consetetur sadipscing elitr sed diam nonumy eirmod tempor invidunt ut labore et dolorest magna aliquyam erat sed diam et accusam justo duo rebum.</p></div>
  <div class="feature" style="left:366px;top:148px"><span class="badge"><svg viewBox="0 0 28 28" fill="none" stroke="#fff" stroke-width="1.6"><rect x="9" y="9" width="10" height="10" rx="1"/><path d="M9 13h10"/></svg></span><h3>Online Appointment</h3><p>Lorem ipsum dolor sit amet, consetetur sadipscing elitr sed diam nonumy eirmod tempor invidunt ut labore et dolorest magna aliquyam erat sed diam et accusam justo duo rebum.</p></div>
  <div class="feature" style="left:106px;top:346px"><span class="badge"><svg viewBox="0 0 28 28" fill="none" stroke="#fff" stroke-width="1.6"><rect x="9" y="9" width="10" height="10" rx="1"/><path d="M9 13h10"/></svg></span><h3>Online Appointment</h3><p>Lorem ipsum dolor sit amet, consetetur sadipscing elitr sed diam nonumy eirmod tempor invidunt ut labore et dolorest magna aliquyam erat sed diam et accusam justo duo rebum.</p></div>
  <div class="feature" style="left:366px;top:346px"><span class="badge"><svg viewBox="0 0 28 28" fill="none" stroke="#fff" stroke-width="1.6"><rect x="9" y="9" width="10" height="10" rx="1"/><path d="M9 13h10"/></svg></span><h3>Online Appointment</h3><p>Lorem ipsum dolor sit amet, consetetur sadipscing elitr sed diam nonumy eirmod tempor invidunt ut labore et dolorest magna aliquyam erat sed diam et accusam justo duo rebum.</p></div>
</section>
<div class="abs why-photo" role="img" aria-label="Photo of two cleaners in aprons and yellow gloves cleaning a kitchen"></div>

<section>
  <h2 class="abs testimonials-title">Clients Testimonals</h2>
  <div class="testimonial" style="left:106px">
    <div class="avatar" role="img" aria-label="Client portrait"></div>
    <p>Lorem ipsum dolor sit amet consetetur sadipscing elitr sed diam nonumy eirmod tempor invidunt ut labore et dolore magna aliquyam erat sed diam voluptua.</p>
    <strong>Dara Lindqvist</strong><span>Maple Row Co.</span>
  </div>
  <div class="testimonial" style="left:622px">
    <div class="avatar" role="img" aria-label="Client portrait"></div>
    <p>Lorem ipsum dolor sit amet consetetur sadipscing elitr sed diam nonumy eirmod tempor invidunt ut labore et dolore magna aliquyam erat sed diam voluptua.</p>
    <strong>Dara Lindqvist</strong><span>Maple Row Co.</span>
  </div>
</section>

<footer class="abs site-footer">© BrightNest, 2016.</footer>

</body>
</html>
```